Real Estate Company
Residential & Commercial
Sales & Property Management

would like to use the logo i uploaded but would really love a black back ground...I think with the gold fleur dis lis and the maroon lettering it would really look great!

Industry/Entity Type

Business

Contact Information for Business Card

Bright Harbor Real Estate Co.
Renata Dubois
Broker/Owner
337-502-4173 Cell
337-618-9034 Office
4172 Pelton Rd Maurice LA 70555

```html
<!DOCTYPE html>
<html lang="en">
<head>
<meta charset="utf-8">
<title>Bright Harbor Real Estate Co. – Business Card</title>
<link rel="stylesheet" href="https://fonts.googleapis.com/css2?family=Aldrich&display=swap">
<style>
  :root {
    --backdrop: #8c8c8c;
    --card: #111111;
    --maroon: #7b2226;
    --gold-light: #f6d63a;
    --gold-dark: #e8b313;
    --gold-text: #e9bd2a;
    --white: #ffffff;
    --soft: #e6e1d8;
  }
  * { box-sizing: border-box; margin: 0; padding: 0; }
  html, body {
    width: 1200px; height: 895px; overflow: hidden;
    background: var(--backdrop);
    font-family: "Aldrich", sans-serif;
  }
  .stage { position: relative; width: 1200px; height: 895px; }
  .card {
    position: absolute; left: 250px;
    width: 700px; height: 400px;
    background: var(--card);
    overflow: hidden;
    box-shadow: 0 6px 18px rgba(0,0,0,.3);
  }
  .card--front { top: 35px; }
  .card--back { top: 460px; }
  .card__art { position: absolute; inset: 0; width: 700px; height: 400px; }

  .brand { position: absolute; display: flex; align-items: center; gap: 14px; color: var(--gold-text); }
  .brand__dot { border-radius: 50%; background: var(--maroon); flex: none; }
  .brand__name { line-height: 1.05; font-weight: 400; }
  .card--front .brand { left: 0; right: 0; top: 140px; justify-content: center; }
  .card--front .brand__dot { width: 56px; height: 56px; }
  .card--front .brand__name { font-size: 40px; }
  .card--back .brand { left: 34px; top: 30px; gap: 10px; }
  .card--back .brand__dot { width: 34px; height: 34px; }
  .card--back .brand__name { font-size: 22px; }

  .person { position: absolute; right: 40px; top: 76px; width: 250px; color: var(--gold-text); }
  .person__name { font-size: 26px; letter-spacing: 2px; }
  .person__title { font-size: 12px; letter-spacing: 1.5px; margin-top: 8px; color: var(--soft); }

  .contact { position: absolute; top: 222px; color: var(--soft); font-size: 15px; line-height: 1.6; letter-spacing: .5px; }
  .contact--web { left: 24px; font-size: 14px; }
  .contact--address { left: 258px; }
  .contact--phone { left: 490px; font-size: 17px; letter-spacing: 1.5px; }
</style>
</head>
<body>
<main class="stage">

  <section class="card card--front" aria-label="Business card front">
    <svg class="card__art" viewBox="0 0 700 400" aria-hidden="true">
      <rect class="band band--top" x="0" y="0" width="700" height="70" fill="var(--maroon)"/>
      <rect class="band band--bottom" x="0" y="330" width="700" height="70" fill="var(--maroon)"/>
      <polyline points="412,0 434,35 412,70" fill="none" stroke="var(--white)" stroke-width="6"/>
      <polyline points="228,330 250,365 228,400" fill="none" stroke="var(--white)" stroke-width="6"/>
      <polyline points="560,330 582,365 560,400" fill="none" stroke="var(--white)" stroke-width="6"/>
    </svg>
    <div class="brand">
      <span class="brand__dot"></span>
      <span class="brand__name">Bright Harbor<br>Real Estate Co.</span>
    </div>
  </section>

  <section class="card card--back" aria-label="Business card back">
    <svg class="card__art" viewBox="0 0 700 400" aria-hidden="true">
      <defs>
        <linearGradient id="goldBand" x1="0" y1="0" x2="0" y2="1">
          <stop offset="0" stop-color="var(--gold-light)"/>
          <stop offset="1" stop-color="var(--gold-dark)"/>
        </linearGradient>
      </defs>
      <polygon class="ribbon" points="0,150 216,150 238,175 216,200 0,200" fill="url(#goldBand)"/>
      <polygon class="ribbon" points="226,150 448,150 470,175 448,200 226,200 248,175" fill="url(#goldBand)"/>
      <polygon class="ribbon" points="458,150 700,150 700,200 458,200 480,175" fill="url(#goldBand)"/>
      <rect class="band band--bottom" x="0" y="325" width="700" height="75" fill="var(--maroon)"/>

      <g class="icon icon--globe" fill="none" stroke="var(--white)" stroke-width="2.2" transform="translate(40 175)">
        <circle r="12"/>
        <ellipse rx="5.5" ry="12"/>
        <line x1="-12" y1="0" x2="12" y2="0"/>
        <line x1="-10" y1="-6" x2="10" y2="-6"/>
        <line x1="-10" y1="6" x2="10" y2="6"/>
      </g>
      <g class="icon icon--pin" transform="translate(300 175)">
        <path d="M0,13 C-4,6 -10,0 -10,-5 A10,10 0 0 1 10,-5 C10,0 4,6 0,13 Z" fill="var(--white)"/>
        <circle cx="0" cy="-5" r="3.6" fill="var(--gold-dark)"/>
      </g>
      <g class="icon icon--phone" fill="none" stroke="var(--white)" stroke-width="2.2" transform="translate(540 175)">
        <rect x="-8" y="-14" width="16" height="28" rx="3"/>
        <line x1="-3" y1="-10" x2="3" y2="-10"/>
        <circle cx="0" cy="9" r="1.4" fill="var(--white)"/>
      </g>
    </svg>

    <div class="brand">
      <span class="brand__dot"></span>
      <span class="brand__name">Bright Harbor<br>Real Estate Co.</span>
    </div>

    <div class="person">
      <p class="person__name">RENATA DUBOIS</p>
      <p class="person__title">BROKER/OWNER</p>
    </div>

    <p class="contact contact--web">renata@brightharbor.com<br>www.brightharborrealty.com</p>
    <p class="contact contact--address">4172 Pelton Rd<br>Maurice LA 70555</p>
    <p class="contact contact--phone">337-502-4173<br>337-618-9034</p>
  </section>

</main>
</body>
</html>
```